Eyeglasses company needs Professional packaging design for small shipping box

Update 09/11/18 Looking for Black box with black or white lettering. See new pictures.

Update 09.10.18
The previous color scheme is just not working and we have decided to make things simpler and go with a all black box on the outside. All Black with smaller white lettering. The inside of the box white and possible glasses pattern (see new attachment) white, fun and simple on the inside. Looking for creative saying on sides of box and on the inside top.

Update-Deadline extended.

Hi, We have extended the deadline 1 week. We need more designs, more professional and simple with little bit of cuteness and fun sayings about glasses and vision on the side of the box.

All black box with subtle White lettering will WIN- Looking for Hints of the creative characters and logos. Looking for CLEAN, SIMPLE, A little cute, a little fun, Professional. Business Casual.

I've provided a sample image of the box I'm looking for in the brief, still looking for someone to copy that box and make minor adjustments with hints of creativity.

I really need the dieline template on the submissions because I will use that template to submit to the box company.

We are a new company called VARNEK based in Southern California that sells high quality, affordable eyeglasses online. We also replace old prescription lenses with new ones in patients own frame. We need a CUTE FUN box to send the frames to the customer!

Box size is 8 inches x 5 inches x 2 inches

*Important- We're using BOXTRELLO.COM for our creative boxes. They have requirements. Here is the information from them.

We accept both of those file types, including .PNG. Be sure that all artwork/images are at least 300ppi for best print results. Dieline template- instructions in the link regarding artwork that will help. https://boxtrello.helpdeskly.com/support/solutions/articles/48100027731-design-setup-and-orientation

Hi there,
Here’s the customizable box template you requested. If you have any questions, or when you’re ready to place an order, drop us a line with your files attached and one of our team members will get back to you in a jiffy.
In the meantime, here’s a brief rundown of the artwork set-up guidelines for working with our templates:
• Files should be in CMYK mode (not RGB).
• Be sure to expand all fonts and text to shapes (vectors)* — no live text, please and thank you.
• Embed all images in the document or send the links for the artwork source files. This will prevent any missing links when we go to press.
• Your designs should have at least a 0.25-inch bleed in areas where the graphic exceeds the dieline.
• Dielines should be on a separate layer, visible to prepress for set up. If they are distracting while you are working on or proofing the file, you can turn off their visibility by using the "eye" icon in the Layers palette.
• Send your file(s) in a format that is readable in Adobe Illustrator CS6. If exporting from Adobe Illustrator Creative Cloud, you can down-save to CS6 in the 'Save As' menu.
When your artwork is finished, please send us an email with the artwork attached. We will review the files and provide you with a custom checkout link to use.
• Pro Tip: We created a handy Adobe Illustrator script that will automatically expand your fonts and increase your text size so that they adhere to our artwork guidelines. Download it here: link
Ready? Set. Design!
We can't wait to see what you create!
Your pals at Boxtrello

Target Market(s)

20-60 yo male and female that wear eyeglasses

Industry/Entity Type

Eyewear

Font styles to use
Serif

Colors
000000
eaeaea
ffffff
aaaaaa
1b1b1b
5c5c5c
fefefe
474747
333333

Requirements
Must have
• Must Have:
• - Must be neutral for both genders but cute is a plus.
• - Attached is a sample box of the exact size and type of shipping box.
• - The shipping box will contain the eyeglass frames and case.
• - The dimensions of the shipping box are 8" x 5" x 2"
• -Looking for all black box with white lettering (photo attached). This is creative open project.
• Our website is under construction. Varnekeyewear.com
• Looking for cute fun words on the sides/inside of the box including our name and website.
• Examples
• VARNEK
• Varnekeyewear.com
• Sight, sealed, delivered
• Eyecharts
• Eyelashes
• Anything eye related!!!
• etc etc.
• Looking for creative words on the side of the box and inside the box.
• Front
• Left
• Back
• Right
• Top
• Bottom
• Interior Top
• Interior Bottom
• - Cute, cool, simple fun designs. Subtle Designs on the inside of the box.
• - I'm trying to simplify a complicated process with doctors, prescriptions, insurance.
• - So a simplified first impression is best.

```html
<!DOCTYPE html>
<html lang="en">
<head>
<meta charset="utf-8">
<title>Varnek Mailer Box Dieline</title>
<link href="https://fonts.googleapis.com/css2?family=Josefin+Sans:wght@400;600&family=Roboto:wght@400&display=swap" rel="stylesheet">
<style>
  :root {
    --bg: #0e1013;
    --cut: #7dc242;
    --fold: #e0261f;
    --safe: #000000;
    --dim: #3d63c4;
    --ink: #ffffff;
  }
  html, body { margin: 0; padding: 0; overflow: hidden; background: var(--bg); }
  .canvas { width: 1200px; height: 1133px; display: block; }
  .cut { fill: none; stroke: var(--cut); stroke-width: 1.6; }
  .fold { fill: none; stroke: var(--fold); stroke-width: 1.6; }
  .safe { fill: none; stroke: var(--safe); stroke-width: 1.6; }
  .dim-line { stroke: var(--dim); stroke-width: 1.2; fill: none; }
  .ext-line { stroke: var(--dim); stroke-width: 1; }
  .dim-label { fill: var(--dim); font-family: "Roboto", sans-serif; font-size: 30px; text-anchor: middle; }
  .dim-label .frac { font-size: 19px; }
  .dim-label.edge { text-anchor: end; }
  .spec-note { fill: var(--dim); font-family: "Roboto", sans-serif; font-size: 17px; }
  .brand-name { fill: var(--ink); font-family: "Josefin Sans", sans-serif; font-weight: 400; text-anchor: middle; }
  .brand-url { fill: var(--ink); font-family: "Josefin Sans", sans-serif; font-weight: 600; font-size: 13px; text-anchor: middle; }
  .side-saying { fill: var(--ink); font-family: "Josefin Sans", sans-serif; font-weight: 400; font-size: 15px; letter-spacing: 2px; text-anchor: middle; }
</style>
</head>
<body>
<svg class="canvas" viewBox="0 0 1500 1416" xmlns="http://www.w3.org/2000/svg">
  <defs>
    <marker id="arrow" viewBox="0 0 10 10" refX="10" refY="5" markerWidth="14" markerHeight="10" orient="auto-start-reverse" markerUnits="userSpaceOnUse">
      <path d="M0 1 L10 5 L0 9" fill="none" stroke="#3d63c4" stroke-width="1.2"/>
    </marker>
  </defs>

  <g class="dieline-cut">
    <path class="cut" d="M358 186 L232 192 Q202 190 205 160 Q218 70 320 28 L945 28 Q1072 60 1088 150 Q1092 180 1062 185 L1022 196 Q1092 202 1095 255 L1095 500 Q1092 552 1050 557 L965 565 L965 683 L1100 683 Q1105 687 1110 687 L1255 687 Q1273 690 1273 705 L1273 815 L1283 815 L1283 945 L1273 945 L1273 1060 Q1272 1075 1255 1077 L1110 1077 L960 1080 L960 1225 L332 1225 L332 1080 L180 1077 L40 1077 Q22 1075 20 1060 L20 945 L10 945 L10 815 L20 815 L20 705 Q22 689 40 687 L180 687 Q186 683 190 683 L328 683 L328 565 L235 552 Q200 548 198 505 L198 258 Q200 205 268 196 Z"/>
  </g>

  <g class="dieline-safe">
    <path class="safe" d="M356 46 L945 46 Q1050 80 1072 160 Q1070 172 1050 176 L935 186"/>
    <path class="safe" d="M356 46 Q250 90 222 160 Q222 172 240 176 L356 186"/>
    <path class="safe" d="M935 198 L1060 218 Q1078 232 1078 262 L1078 505 Q1074 538 1050 544 L935 553"/>
    <path class="safe" d="M358 198 L232 218 Q215 232 215 262 L215 505 Q218 538 240 544 L358 553"/>
    <rect class="safe" x="170" y="557" width="158" height="126" rx="6"/>
    <rect class="safe" x="965" y="557" width="158" height="126" rx="6"/>
    <rect class="safe" x="37" y="704" width="145" height="356" rx="4"/>
    <rect class="safe" x="1110" y="704" width="147" height="356" rx="4"/>
    <rect class="safe" x="342" y="830" width="14" height="104" rx="6"/>
    <rect class="safe" x="936" y="830" width="14" height="104" rx="6"/>
    <rect class="safe" x="170" y="1082" width="162" height="125" rx="6"/>
    <rect class="safe" x="960" y="1082" width="162" height="125" rx="6"/>
    <rect class="safe" x="28" y="830" width="10" height="104"/>
    <rect class="safe" x="1257" y="830" width="10" height="104"/>
  </g>

  <g class="dieline-fold">
    <line class="fold" x1="346" y1="45" x2="346" y2="186"/>
    <line class="fold" x1="946" y1="45" x2="946" y2="186"/>
    <rect class="fold" x="358" y="190" width="575" height="365"/>
    <rect class="fold" x="346" y="555" width="600" height="147"/>
    <line class="fold" x1="182" y1="702" x2="182" y2="1060"/>
    <line class="fold" x1="194" y1="702" x2="194" y2="1060"/>
    <line class="fold" x1="342" y1="702" x2="342" y2="1060"/>
    <line class="fold" x1="950" y1="702" x2="950" y2="1060"/>
    <line class="fold" x1="1098" y1="702" x2="1098" y2="1060"/>
    <line class="fold" x1="1110" y1="702" x2="1110" y2="1060"/>
    <rect class="fold" x="350" y="1062" width="592" height="145"/>
  </g>

  <g class="artwork">
    <text class="brand-url" x="644" y="98" transform="translate(0 201) scale(1 -1)">VARNEKEYEWEAR.COM</text>
    <text class="brand-name" x="650" y="385" font-size="52" letter-spacing="6">VARNEK</text>
    <text class="brand-name" font-size="26" letter-spacing="3" transform="translate(260 873) rotate(90)">VARNEK</text>
    <text class="brand-name" font-size="26" letter-spacing="3" transform="translate(1034 873) rotate(-90)">VARNEK</text>
    <text class="side-saying" transform="translate(112 880) rotate(90)">SIGHT, SEALED, DELIVERED</text>
    <text class="side-saying" transform="translate(1160 880) rotate(-90)">EYE LOVE YOUR STYLE</text>
  </g>

  <text class="spec-note" x="523" y="288">Flute E</text>
  <text class="spec-note" x="523" y="309">Inside dimension 8x5x2  in</text>

  <g class="extensions">
    <line class="ext-line" x1="975" y1="45" x2="1482" y2="45"/>
    <line class="ext-line" x1="945" y1="188" x2="1370" y2="188"/>
    <line class="ext-line" x1="1128" y1="555" x2="1370" y2="555"/>
    <line class="ext-line" x1="1260" y1="702" x2="1368" y2="702"/>
    <line class="ext-line" x1="1135" y1="1207" x2="1482" y2="1207"/>
    <line class="ext-line" x1="37" y1="1080" x2="37" y2="1310"/>
    <line class="ext-line" x1="180" y1="1080" x2="180" y2="1310"/>
    <line class="ext-line" x1="194" y1="1080" x2="194" y2="1310"/>
    <line class="ext-line" x1="342" y1="1080" x2="342" y2="1310"/>
    <line class="ext-line" x1="350" y1="1210" x2="350" y2="1310"/>
    <line class="ext-line" x1="942" y1="1210" x2="942" y2="1310"/>
    <line class="ext-line" x1="950" y1="1080" x2="950" y2="1310"/>
    <line class="ext-line" x1="1098" y1="1080" x2="1098" y2="1310"/>
    <line class="ext-line" x1="1110" y1="1080" x2="1110" y2="1310"/>
    <line class="ext-line" x1="1255" y1="1080" x2="1255" y2="1310"/>
    <line class="ext-line" x1="28" y1="1080" x2="28" y2="1385"/>
    <line class="ext-line" x1="1265" y1="1080" x2="1265" y2="1385"/>
    <line class="ext-line" x1="903" y1="828" x2="940" y2="828"/>
    <line class="ext-line" x1="903" y1="935" x2="940" y2="935"/>
    <line class="ext-line" x1="1210" y1="828" x2="1242" y2="828"/>
    <line class="ext-line" x1="1210" y1="935" x2="1242" y2="935"/>
    <line class="ext-line" x1="260" y1="683" x2="275" y2="683"/>
    <line class="ext-line" x1="260" y1="702" x2="275" y2="702"/>
  </g>

  <g class="dimensions">
    <line class="dim-line" x1="346" y1="146" x2="612" y2="146" marker-start="url(#arrow)"/>
    <line class="dim-line" x1="680" y1="146" x2="946" y2="146" marker-end="url(#arrow)"/>
    <line class="dim-line" x1="1362" y1="45" x2="1362" y2="100" marker-start="url(#arrow)"/>
    <line class="dim-line" x1="1362" y1="138" x2="1362" y2="188" marker-end="url(#arrow)"/>
    <line class="dim-line" x1="1362" y1="188" x2="1362" y2="355" marker-start="url(#arrow)"/>
    <line class="dim-line" x1="1362" y1="395" x2="1362" y2="555" marker-end="url(#arrow)"/>
    <line class="dim-line" x1="1362" y1="555" x2="1362" y2="610" marker-start="url(#arrow)"/>
    <line class="dim-line" x1="1362" y1="648" x2="1362" y2="702" marker-end="url(#arrow)"/>
    <line class="dim-line" x1="1475" y1="45" x2="1475" y2="608" marker-start="url(#arrow)"/>
    <line class="dim-line" x1="1475" y1="648" x2="1475" y2="1207" marker-end="url(#arrow)"/>
    <line class="dim-line" x1="358" y1="505" x2="598" y2="505" marker-start="url(#arrow)"/>
    <line class="dim-line" x1="668" y1="505" x2="933" y2="505" marker-end="url(#arrow)"/>
    <line class="dim-line" x1="933" y1="495" x2="972" y2="495" marker-start="url(#arrow)"/>
    <line class="dim-line" x1="1040" y1="495" x2="1078" y2="495" marker-end="url(#arrow)"/>
    <line class="dim-line" x1="346" y1="604" x2="612" y2="604" marker-start="url(#arrow)"/>
    <line class="dim-line" x1="680" y1="604" x2="946" y2="604" marker-end="url(#arrow)"/>
    <line class="dim-line" x1="170" y1="635" x2="222" y2="635" marker-start="url(#arrow)"/>
    <line class="dim-line" x1="295" y1="635" x2="346" y2="635" marker-end="url(#arrow)"/>
    <line class="dim-line" x1="896" y1="658" x2="946" y2="658" marker-end="url(#arrow)"/>
    <line class="dim-line" x1="1002" y1="658" x2="952" y2="658" marker-end="url(#arrow)"/>
    <line class="dim-line" x1="267" y1="648" x2="267" y2="683" marker-end="url(#arrow)"/>
    <line class="dim-line" x1="267" y1="740" x2="267" y2="702" marker-end="url(#arrow)"/>
    <line class="dim-line" x1="690" y1="702" x2="690" y2="862" marker-start="url(#arrow)"/>
    <line class="dim-line" x1="690" y1="902" x2="690" y2="1062" marker-end="url(#arrow)"/>
    <line class="dim-line" x1="910" y1="780" x2="910" y2="828" marker-end="url(#arrow)"/>
    <line class="dim-line" x1="910" y1="985" x2="910" y2="935" marker-end="url(#arrow)"/>
    <line class="dim-line" x1="1217" y1="780" x2="1217" y2="828" marker-end="url(#arrow)"/>
    <line class="dim-line" x1="1217" y1="985" x2="1217" y2="935" marker-end="url(#arrow)"/>
    <line class="dim-line" x1="0" y1="993" x2="20" y2="993" marker-end="url(#arrow)"/>
    <line class="dim-line" x1="87" y1="993" x2="37" y2="993" marker-end="url(#arrow)"/>
    <line class="dim-line" x1="130" y1="1010" x2="182" y2="1010" marker-end="url(#arrow)"/>
    <line class="dim-line" x1="245" y1="1010" x2="194" y2="1010" marker-end="url(#arrow)"/>
    <line class="dim-line" x1="290" y1="1000" x2="342" y2="1000" marker-end="url(#arrow)"/>
    <line class="dim-line" x1="408" y1="1000" x2="356" y2="1000" marker-end="url(#arrow)"/>
    <line class="dim-line" x1="892" y1="1050" x2="944" y2="1050" marker-end="url(#arrow)"/>
    <line class="dim-line" x1="1002" y1="1050" x2="952" y2="1050" marker-end="url(#arrow)"/>
    <line class="dim-line" x1="688" y1="1062" x2="688" y2="1115" marker-start="url(#arrow)"/>
    <line class="dim-line" x1="688" y1="1155" x2="688" y2="1207" marker-end="url(#arrow)"/>
    <line class="dim-line" x1="37" y1="1302" x2="78" y2="1302" marker-start="url(#arrow)"/>
    <line class="dim-line" x1="142" y1="1302" x2="180" y2="1302" marker-end="url(#arrow)"/>
    <line class="dim-line" x1="194" y1="1296" x2="236" y2="1296" marker-start="url(#arrow)"/>
    <line class="dim-line" x1="300" y1="1296" x2="342" y2="1296" marker-end="url(#arrow)"/>
    <line class="dim-line" x1="350" y1="1293" x2="612" y2="1293" marker-start="url(#arrow)"/>
    <line class="dim-line" x1="680" y1="1293" x2="942" y2="1293" marker-end="url(#arrow)"/>
    <line class="dim-line" x1="950" y1="1291" x2="992" y2="1291" marker-start="url(#arrow)"/>
    <line class="dim-line" x1="1056" y1="1291" x2="1098" y2="1291" marker-end="url(#arrow)"/>
    <line class="dim-line" x1="1110" y1="1293" x2="1150" y2="1293" marker-start="url(#arrow)"/>
    <line class="dim-line" x1="1216" y1="1293" x2="1255" y2="1293" marker-end="url(#arrow)"/>
    <line class="dim-line" x1="28" y1="1376" x2="612" y2="1376" marker-start="url(#arrow)"/>
    <line class="dim-line" x1="680" y1="1376" x2="1265" y2="1376" marker-end="url(#arrow)"/>
    <polyline class="dim-line" points="1140,210 1085,210 1065,175" marker-end="url(#arrow)"/>
    <polyline class="dim-line" points="150,573 200,573 228,535" marker-end="url(#arrow)"/>
  </g>

  <g class="dimension-labels">
    <text class="dim-label" x="646" y="158">8<tspan class="frac" dy="-10">7</tspan><tspan class="frac" dy="10">/16</tspan></text>
    <text class="dim-label" x="1364" y="130">2<tspan class="frac" dy="-10">1</tspan><tspan class="frac" dy="10">/32</tspan></text>
    <text class="dim-label" x="1160" y="218"><tspan class="frac" dy="-6">1</tspan><tspan class="frac" dy="6">/4</tspan><tspan class="frac" dy="-14">R</tspan></text>
    <text class="dim-label" x="1364" y="385">5<tspan class="frac" dy="-10">1</tspan><tspan class="frac" dy="10">/8</tspan></text>
    <text class="dim-label" x="1362" y="640">2<tspan class="frac" dy="-10">1</tspan><tspan class="frac" dy="10">/16</tspan></text>
    <text class="dim-label edge" x="1496" y="638">16<tspan class="frac" dy="-10">5</tspan><tspan class="frac" dy="10">/16</tspan></text>
    <text class="dim-label" x="633" y="518">8<tspan class="frac" dy="-10">1</tspan><tspan class="frac" dy="10">/16</tspan></text>
    <text class="dim-label" x="1006" y="508">2<tspan class="frac" dy="-10">1</tspan><tspan class="frac" dy="10">/32</tspan></text>
    <text class="dim-label" x="126" y="582"><tspan class="frac" dy="-6">1</tspan><tspan class="frac" dy="6">/2</tspan><tspan class="frac" dy="-14">R</tspan></text>
    <text class="dim-label" x="646" y="616">8<tspan class="frac" dy="-10">7</tspan><tspan class="frac" dy="10">/16</tspan></text>
    <text class="dim-label" x="258" y="646">2<tspan class="frac" dy="-10">15</tspan><tspan class="frac" dy="10">/32</tspan></text>
    <text class="dim-label" x="1025" y="668"><tspan class="frac" dy="-6">1</tspan><tspan class="frac" dy="6">/16</tspan></text>
    <text class="dim-label" x="267" y="782"><tspan class="frac" dy="-6">1</tspan><tspan class="frac" dy="6">/32</tspan></text>
    <text class="dim-label" x="690" y="893">5<tspan class="frac" dy="-10">1</tspan><tspan class="frac" dy="10">/16</tspan></text>
    <text class="dim-label" x="912" y="893">1<tspan class="frac" dy="-10">1</tspan><tspan class="frac" dy="10">/2</tspan></text>
    <text class="dim-label" x="1219" y="893">1<tspan class="frac" dy="-10">1</tspan><tspan class="frac" dy="10">/2</tspan></text>
    <text class="dim-label" x="105" y="1002"><tspan class="frac" dy="-6">1</tspan><tspan class="frac" dy="6">/8</tspan></text>
    <text class="dim-label" x="268" y="1020"><tspan class="frac" dy="-6">3</tspan><tspan class="frac" dy="6">/16</tspan></text>
    <text class="dim-label" x="430" y="1010"><tspan class="frac" dy="-6">7</tspan><tspan class="frac" dy="6">/32</tspan></text>
    <text class="dim-label" x="1020" y="1060"><tspan class="frac" dy="-6">1</tspan><tspan class="frac" dy="6">/8</tspan></text>
    <text class="dim-label" x="688" y="1146">2<tspan class="frac" dy="-10">1</tspan><tspan class="frac" dy="10">/32</tspan></text>
    <text class="dim-label" x="110" y="1313">2<tspan class="frac" dy="-10">1</tspan><tspan class="frac" dy="10">/32</tspan></text>
    <text class="dim-label" x="268" y="1307">2<tspan class="frac" dy="-10">1</tspan><tspan class="frac" dy="10">/16</tspan></text>
    <text class="dim-label" x="646" y="1304">8<tspan class="frac" dy="-10">5</tspan><tspan class="frac" dy="10">/16</tspan></text>
    <text class="dim-label" x="1024" y="1302">2<tspan class="frac" dy="-10">1</tspan><tspan class="frac" dy="10">/16</tspan></text>
    <text class="dim-label" x="1184" y="1306">2<tspan class="frac" dy="-10">1</tspan><tspan class="frac" dy="10">/32</tspan></text>
    <text class="dim-label" x="646" y="1387">17<tspan class="frac" dy="-10">3</tspan><tspan class="frac" dy="10">/8</tspan></text>
  </g>
</svg>
</body>
</html>
```